Audit/Compliance company needs Business Card Template

We are after a Business Card Template that we can modify internally to update details as people change positions.
We are an Australian based company specalising in Auditing and Quality/OHS systems development. - See www.kelvaranorth.com.au for more information
We would like the desings to be based around our logo and colours assocaited with it (attached for your information) however we are very open as to how the cards are designed.
We are looking for something quite edgy and mordern but it must have a professional/compliance feel to it (if possible).
The main details we would like to include within the card template are:
Name
Position Title
Postal Address
Phone Number
Mobile Number
Email Address
Website
The cards will be printed through tally press on Glossy paper so it should reflect the requirements below
Full Bleed Size (starting document size)
90 x 52 mm
1062 x 615 pixels
Document Trim Size (final size after being cut)
87 x 49 mm
1028 x 579 pixels
Resolution
300 DPI

```html
<!DOCTYPE html>
<html lang="en">
<head>
<meta charset="utf-8">
<title>Kelvara North – Business Card Template</title>
<link rel="stylesheet" href="https://fonts.googleapis.com/css2?family=Fredoka:wght@600;700&family=Arimo:wght@400&display=swap">
<style>
  :root {
    --card-red: #e30b17;
    --deep-red: #a8242c;
    --street-dark: #2b2220;
    --brick-cream: #fcd5a5;
    --paper: #ffffff;
    --ink: #111111;
    --rule-cream: #f6c78f;
    --icon-grey: #9aa3ad;
  }
  * { margin: 0; padding: 0; box-sizing: border-box; }
  html, body {
    width: 1200px; height: 900px; overflow: hidden;
    background: var(--paper);
  }
  .canvas { position: relative; width: 1200px; height: 900px; }

  .card { position: absolute; top: 5px; width: 563px; height: 324px; overflow: hidden; }

  /* Front */
  .card--front { left: 0; background: var(--card-red); }
  .street-scene {
    position: absolute; left: 0; top: 0; width: 563px; height: 142px;
    background: linear-gradient(180deg, #7a1a1a 0%, var(--street-dark) 55%, #5a1717 100%);
  }
  .paint-splatter {
    position: absolute; left: 0; top: 140px; width: 135px; height: 184px;
    background: linear-gradient(180deg, rgba(168,36,44,0.35), rgba(168,36,44,0.85));
    border-radius: 0 60px 40px 0;
  }
  .holder-name {
    position: absolute; left: 95px; top: 140px;
    font-family: "Fredoka", sans-serif; font-weight: 700;
    font-size: 38px; color: var(--paper); letter-spacing: 1px;
  }
  .holder-title {
    position: absolute; left: 88px; top: 188px;
    font-family: "Fredoka", sans-serif; font-weight: 700;
    font-size: 18px; color: var(--paper);
  }
  .divider {
    position: absolute; left: 245px; top: 210px; width: 3px; height: 114px;
    background: var(--rule-cream);
  }
  .contact-list {
    position: absolute; right: 200px; top: 206px; list-style: none; text-align: right;
    font-family: "Fredoka", sans-serif; font-weight: 600; font-size: 12.5px;
    color: var(--paper); line-height: 30px;
  }

  /* Back */
  .card--back {
    left: 637px;
    background: linear-gradient(135deg, var(--paper) 0%, #fde9cf 45%, var(--paper) 100%);
  }
  .brick-wall {
    position: absolute; inset: 0;
    background: linear-gradient(90deg, rgba(252,213,165,0.2), rgba(252,213,165,0.55));
  }
  .halftone-splash { position: absolute; left: 0; top: 0; }
  .web-address {
    position: absolute; left: 254px; top: 195px;
    font-family: "Arimo", sans-serif; font-size: 50px; color: var(--ink);
  }
  .social-list {
    position: absolute; right: 30px; top: 20px; list-style: none;
    font-family: "Fredoka", sans-serif; font-weight: 700; font-size: 12.5px; color: var(--ink);
  }
  .social-list li { display: flex; align-items: center; justify-content: flex-end; height: 29.6px; gap: 9px; }
  .social-list .dot { width: 26px; height: 26px; border-radius: 50%; background: var(--icon-grey); }
</style>
</head>
<body>
<main class="canvas">
  <section class="card card--front">
    <div class="street-scene" role="img" aria-label="Street scene with parked cars in front of city buildings"></div>
    <div class="paint-splatter" role="img" aria-label="Dark red paint splatter"></div>
    <h1 class="holder-name">Name</h1>
    <p class="holder-title">Position Title</p>
    <div class="divider"></div>
    <ul class="contact-list">
      <li>Postal Adress</li>
      <li>Phone Number</li>
      <li>Mobile Number</li>
      <li>E-Mail Adress</li>
    </ul>
  </section>

  <section class="card card--back">
    <div class="brick-wall" role="img" aria-label="Cream painted brick wall texture"></div>
    <svg class="halftone-splash" width="260" height="324" viewBox="0 0 260 324" role="img" aria-label="Red halftone paint splash with stars">
      <path d="M0 0 H80 C120 40 140 90 160 130 C180 170 200 200 190 240 C180 280 200 300 190 324 H0 Z" fill="var(--card-red)"/>
      <path d="M20 150 C60 130 120 150 150 190 C160 230 130 270 90 290 C50 300 20 280 0 260 V160 Z" fill="var(--deep-red)"/>
    </svg>
    <p class="web-address">web</p>
    <ul class="social-list">
      <li>social <span class="dot"></span></li>
      <li>social <span class="dot"></span></li>
      <li>social <span class="dot"></span></li>
      <li>social <span class="dot"></span></li>
      <li>social <span class="dot"></span></li>
    </ul>
  </section>
</main>
</body>
</html>
```